New telco company needs a product page

We need to design two pages - one index and one inner.

We are a new telco company and we have developed our own phone. We will be selling our services and the phone on this site.

The design should be easy to understand and use, following the latest trends in Web design, be clean. It should communicate professionalism and integrity.

The name of our company is VORO which stands for Value Over Rush Often. The design should follow this principle.

Our company logo is attached. I can send it in other colors/sizes - let me know.

Target Market(s)

Aging population (70+), middle-aged with parents and grandparents.

Industry/Entity Type

It Company

Requirements
Must have
• index page, inner page, flat, clean, Pellucor 5 style / ZEB style (quintel.example), easy navigation, fluid layout, CSS, tableless
Should not have
• should not use old fonts, should not use old-style design, should not have animation, should not look like QDX or Bimzo (too busy)

```html
<!DOCTYPE html>
<html lang="en">
<head>
<meta charset="utf-8">
<title>VORO Solace Q2</title>
<link rel="stylesheet" href="https://fonts.googleapis.com/css2?family=Ubuntu:wght@300;400;500;700&display=swap">
<style>
:root{
  --black:#05080b;
  --white:#ffffff;
  --ink:#1c1c1c;
  --muted:#6a6a6a;
  --faint:#b9b9b9;
  --blue:#2a7fc0;
  --link:#2478b4;
  --footer:#ebebeb;
  --rule:#d6d6d6;
}
*{margin:0;padding:0;box-sizing:border-box}
html,body{width:1200px;height:1029px;overflow:hidden;background:var(--white)}
body{font-family:"Ubuntu",sans-serif;color:var(--ink);position:relative}
a{text-decoration:none;color:inherit}
.site-header{position:absolute;left:0;top:0;width:1200px;height:78px;background:var(--black)}
.brand{position:absolute;left:197px;top:14px;color:var(--white);font-weight:300;font-size:40px;letter-spacing:-1px;display:flex;align-items:center;gap:8px}
.brand-dot{width:10px;height:10px;border-radius:50%;background:#bdbdbd}
.main-nav a{position:absolute;top:33px;color:var(--white);font-size:10.5px;font-weight:500;letter-spacing:.1px}
.nav-chevron{position:absolute;left:421px;top:35px}
.lang{position:absolute;left:877px;top:33px;color:#cfcfcf;font-size:11px}
.flag{position:absolute;left:934px;top:35px}
.search{position:absolute;left:982px;top:32px}
.hero{position:absolute;left:0;top:78px;width:1200px;height:472px;background:linear-gradient(180deg,#9fb0b4 0%,#c9c2a4 35%,#b7a47a 55%,#7a6a4d 80%,#5f5139 100%)}
.hero-phones{position:absolute;left:197px;top:145px;width:250px;height:352px;border-radius:30px;background:linear-gradient(135deg,#4a4a4a,#0d0d0d 60%,#222)}
.hero-copy{position:absolute;left:522px;top:158px;color:var(--black)}
.hero-model{font-size:30px;font-weight:400;line-height:36px}
.hero-model b{font-weight:500}
.hero-title{margin-top:6px;font-size:45px;font-weight:500;line-height:48px;letter-spacing:.3px}
.feature-box{position:absolute;left:524px;top:320px;width:307px;height:81px;background:rgba(110,92,70,.45);color:#f3eee4;font-size:12px;line-height:14px;display:grid;grid-template-columns:130px 150px;row-gap:12px;padding:20px 0 0 23px;list-style:none}
.cta{position:absolute;left:523px;top:423px;width:168px;height:42px;background:var(--blue);color:var(--white);font-size:16px;display:flex;align-items:center;padding-left:15px;gap:12px}
.cta-alt{position:absolute;left:714px;top:438px;color:var(--white);font-size:12px}
.cta-alt b{margin-left:16px;font-weight:500}
.product-tabs{position:absolute;left:198px;top:550px;width:804px;height:77px;border-bottom:1px solid var(--rule)}
.tab{position:absolute;top:28px;font-size:19px;color:var(--faint);white-space:nowrap}
.tab b{font-weight:500}
.tab.active{color:var(--ink)}
.tab-edge{position:absolute;left:165px;top:0;width:24px;height:76px;background:linear-gradient(90deg,rgba(0,0,0,.09),rgba(0,0,0,0))}
.promo{position:absolute;top:668px;width:240px}
.promo h3{font-size:16px;font-weight:500;margin-bottom:8px}
.promo p{font-size:11.5px;color:var(--muted);line-height:17px}
.promo a{display:inline-block;margin-top:11px;font-size:12px;color:var(--link);font-weight:500}
.promo-phone{position:absolute;left:622px;top:692px;width:74px;height:74px;border-radius:8px;background:linear-gradient(135deg,#555,#111)}
.promo-person{position:absolute;left:850px;top:654px;width:150px;height:116px;background:linear-gradient(90deg,rgba(220,226,232,0),#d8dde2 35%,#b99676 70%,#2a2a2e)}
.site-footer{position:absolute;left:0;top:822px;width:1200px;height:207px;background:var(--footer)}
.footer-col{position:absolute;top:31px;font-size:11.5px;color:var(--muted);line-height:17px}
.footer-col h4{font-size:12px;font-weight:500;color:var(--ink);margin-bottom:6px}
.footer-brand{position:absolute;left:863px;top:22px;color:var(--white);font-size:40px;font-weight:300}
.copyright{position:absolute;left:848px;top:84px;font-size:10.5px;color:var(--muted);line-height:17px}
.country-row{position:absolute;left:199px;top:148px;width:803px;border-top:1px solid var(--rule);padding-top:13px;font-size:10.5px;color:var(--muted);display:flex}
.country-row strong{color:var(--ink);font-weight:500;font-size:12px;margin-right:17px}
.country-row span{margin-right:10px}
.country-row .select{color:var(--link);font-weight:500}
</style>
</head>
<body>
<header class="site-header">
  <a class="brand" href="#">voro<span class="brand-dot"></span></a>
  <nav class="main-nav">
    <a href="#" style="left:358px">PRODUCTS</a>
    <a href="#" style="left:466px">WHY VORO</a>
    <a href="#" style="left:564px">COMMUNITY</a>
    <a href="#" style="left:663px">SUPPORT</a>
  </nav>
  <svg class="nav-chevron" width="12" height="8" viewBox="0 0 12 8"><path d="M1 1l5 5 5-5" fill="none" stroke="#3d8fd0" stroke-width="2"/></svg>
  <span class="lang">Language</span>
  <svg class="flag" width="12" height="9" viewBox="0 0 12 9"><rect width="12" height="9" fill="#fff"/><rect y="0" width="12" height="1.3" fill="#c8102e"/><rect y="2.6" width="12" height="1.3" fill="#c8102e"/><rect y="5.2" width="12" height="1.3" fill="#c8102e"/><rect y="7.8" width="12" height="1.2" fill="#c8102e"/><rect width="5" height="4.5" fill="#3c3b6e"/></svg>
  <svg class="search" width="16" height="16" viewBox="0 0 16 16"><circle cx="6.5" cy="6.5" r="5" fill="none" stroke="#fff" stroke-width="2"/><path d="M10 10l5 5" stroke="#fff" stroke-width="2.4"/></svg>
</header>

<section class="hero">
  <div role="img" aria-label="Hazy landscape of rolling hills at sunrise" style="position:absolute;inset:0"></div>
</section>
<div class="hero-phones" role="img" aria-label="Two black VORO Solace Q2 smartphones"></div>
<div class="hero-copy">
  <h2 class="hero-model"><b>VORO</b> Solace Q2</h2>
  <h1 class="hero-title">POWERFULL SOLACE<br>SERIES</h1>
</div>
<ul class="feature-box">
  <li>4.3" Home Screen</li><li>Compact One-Hand Use</li>
  <li>Quad Core Chips</li><li>Dual Frontal Speakers</li>
</ul>
<a class="cta" href="#">Meet The Q Max <svg width="8" height="12" viewBox="0 0 8 12"><path d="M1.5 1.5l4.5 4.5-4.5 4.5" fill="none" stroke="#fff" stroke-width="2"/></svg></a>
<span class="cta-alt">Or <b>Watch this video</b></span>

<nav class="product-tabs">
  <span class="tab-edge"></span>
  <a class="tab active" href="#" style="left:0"><b>VORO</b> Solace Q2</a>
  <a class="tab" href="#" style="left:191px"><b>VORO</b> Solace Mini</a>
  <a class="tab" href="#" style="left:394px"><b>VORO</b> Solace Tune Q</a>
  <a class="tab" href="#" style="left:630px"><b>VORO</b> Solace Q3</a>
</nav>

<article class="promo" style="left:199px">
  <h3>VORO Innovation</h3>
  <p>We create superior smartphones<br>with superior features.</p>
  <a href="#">Read more ›</a>
</article>
<article class="promo" style="left:471px">
  <h3>Resources &amp; Driver</h3>
  <p>Our software provides for<br>needs of your handheld</p>
  <a href="#">Visit page ›</a>
</article>
<div class="promo-phone" role="img" aria-label="VORO smartphone"></div>
<div class="promo-person" role="img" aria-label="Smiling support agent in an office"></div>
<article class="promo" style="left:746px">
  <h3>Get Support</h3>
  <p>Watch tutorials, read FAQs<br>and get answers.</p>
  <a href="#">Get help ›</a>
</article>

<footer class="site-footer">
  <div class="footer-col" style="left:199px"><h4>Products</h4>Smartphones<br>Accessories<br>Where to buy</div>
  <div class="footer-col" style="left:320px"><h4>About VORO</h4>Newsroom<br>Company Overview<br>Corporate<br>Investor</div>
  <div class="footer-col" style="left:473px"><h4>Community</h4>VORO Community<br>Sign up</div>
  <div class="footer-col" style="left:592px"><h4>Career</h4>Working at VORO<br>Join us</div>
  <div class="footer-col" style="left:704px"><h4>Support</h4>Support Center<br>Warranty Policy<br>Contact Us</div>
  <div class="footer-brand">voro</div>
  <p class="copyright">Copyright 2013 VORO Corporation.<br>All rights reserved.</p>
  <div class="country-row">
    <strong>Country</strong>
    <span>Malaysia</span><span>Thailand</span><span>Vietnam</span><span>Australia</span><span>India</span><span>Philippines</span><span>Malaysia</span><span>Singapore</span><span class="select">Select Country</span><span>Indonesia</span>
  </div>
</footer>
</body>
</html>
```